Personnel Safety & Tracking Systems by velqor

Create a sales presentation to communicate how velqor can help prospective clients in mining and tunnelling to implement IoT systems and create smart sites which can -

Identify, monitor & locate assets;
- personnel
- equipment
- vehicles

Chapters to include:
- about / why us
- how does it work
- system architecture
- features & benefits
- software & hardware specs
- case studies (see attached)
- testimonials
- pricing

1. Learn more about velqor systems at below link
https://velqor.example/crew-location-for-safety/

2. See uploaded existing presentation docs / case studies -

Note: We are looking for a corporate presentation which communicates clearly what velqor can offer. The system has many facets to incorporate, the key to good design communication will be simplifying what can appear to be a technical topic, deliver a simple product and comprehensive solution.

We require more than a template design, the designer must understand and clearly illustrate the product, new graphics will be required. We are available for guidance and can provide any text/content you require.

Competitors:
https://brindlepath.example (this is the most relevant)
https://www.mavolinkworks.example/shift-buddy-for-safe-mining (this will help you learn about the solution)

Note: The competitor products are rather less versatile and advanced than velqor system, we can provide further briefing, as required.

Target Market(s)

Staff safety and project management teams working for mining and tunnelling companies

Industry/Entity Type

Mining and Tunneling

Requirements
Must have
• System architectural diagrams and illustrations, infographics and visualisation to help communicate - system, features and benefits. Also hardware and software specifications for complete picture of the product.

```html
<!DOCTYPE html>
<html lang="en">
<head>
<meta charset="utf-8">
<title>velqor — Personnel Tracking Solutions deck</title>
<link href="https://fonts.googleapis.com/css2?family=Montserrat:wght@400;600;700;800&family=Open+Sans:wght@400;600&display=swap" rel="stylesheet">
<style>
:root{
  --bg:#8fc5e8;
  --blue:#1e9ad6;
  --blue-dark:#147bb0;
  --ink:#2f3941;
  --slate:#59636c;
  --grey:#eceff2;
  --mid:#c9d0d6;
  --white:#ffffff;
  --tunnel-a:#1d2a33;
  --tunnel-b:#6b5a45;
}
*{box-sizing:border-box;margin:0;padding:0}
html,body{width:1200px;height:2976px;overflow:hidden}
body{background:var(--bg);font-family:"Open Sans",Arial,sans-serif;color:var(--ink);position:relative}
.collage{position:absolute;left:0;top:0;width:1200px;height:872px;
  background:linear-gradient(135deg,#e9eef2 0%,#cfd8df 35%,#3b4650 55%,#1e9ad6 75%,#e8edf1 100%)}
.slide{position:absolute;width:548px;height:308px;overflow:hidden;background:var(--white)}
.col-l{left:40px}.col-r{left:612px}
.r1{top:912px}.r2{top:1248px}.r3{top:1584px}.r4{top:1920px}.r5{top:2256px}.r6{top:2592px}
.photo{position:absolute}
.brand{position:absolute;display:flex;align-items:center;gap:6px;font-family:"Montserrat",sans-serif;font-weight:700;font-size:13px;color:var(--ink)}
.brand i{display:block;width:10px;height:10px;background:var(--blue)}
.brand.light{color:var(--white)}
.h{position:absolute;font-family:"Montserrat",sans-serif;font-weight:800;line-height:1.02;color:var(--ink)}
.h b{color:var(--blue);font-weight:800}
.txt{position:absolute;font-size:7.5px;line-height:1.45;color:var(--slate)}
.lbl{font-family:"Montserrat",sans-serif;font-weight:700;font-size:9px;color:var(--ink);display:block;margin-bottom:2px}
.lbl.blue{color:var(--blue)}
.contact{position:absolute;display:flex}
.contact div{width:70px;height:40px;background:var(--white);font-family:"Montserrat",sans-serif;font-size:8px;font-weight:700;text-align:center;padding-top:8px;color:var(--ink)}
.contact div span{display:block;font-family:"Open Sans",sans-serif;font-weight:400;font-size:6.5px;color:var(--slate);margin-top:3px}
.contact div.on{background:var(--blue);color:var(--white)}
.contact div.on span{color:var(--white)}
.btn{position:absolute;background:var(--blue);color:var(--white);font-family:"Montserrat",sans-serif;font-weight:700;font-size:8px;padding:7px 14px}
.dot{display:inline-block;width:16px;height:16px;border-radius:50%;background:var(--blue);vertical-align:middle;margin-right:6px}
.band{position:absolute;background:var(--grey)}
.price{position:absolute;top:70px;width:84px;height:190px;background:var(--white);box-shadow:0 2px 8px rgba(0,0,0,.15);text-align:center;padding-top:14px}
.price h4{font-family:"Montserrat",sans-serif;font-size:10px}
.price p{font-size:6.5px;color:var(--slate);line-height:1.6;margin:10px 8px}
.price.pro{background:var(--blue);color:var(--white);top:60px;height:210px}
.price.pro p{color:var(--white)}
.price .go{display:inline-block;margin-top:8px;font-size:7px;font-weight:600;border:1px solid currentColor;padding:3px 10px}
.badge{position:absolute;background:var(--white);border-radius:3px}
</style>
</head>
<body>

<div class="collage" role="img" aria-label="Angled arrangement of the deck's slides fanned across the header"></div>

<!-- Row 1 -->
<section class="slide col-l r1" style="background:var(--tunnel-a)">
  <div class="photo" role="img" aria-label="Miners in high-visibility gear walking into a lit tunnel" style="inset:0;background:radial-gradient(circle at 62% 40%,#e7c79a 0%,#a27d55 20%,#3b3934 55%,#161e25 100%)"></div>
  <div class="brand light" style="left:22px;top:20px"><i></i>velqor</div>
  <div class="h" style="left:22px;top:108px;font-size:30px;color:var(--white)">Personnel<br>Tracking<br><b>Solutions</b></div>
  <div class="txt" style="left:22px;top:206px;color:#dfe6ea">Smart sites for mining</div>
  <div class="contact" style="left:22px;top:250px">
    <div>E-mail<span>info@velqor</span></div><div class="on">Website<span>velqor.example</span></div><div>Phone<span>000 000 000</span></div>
  </div>
</section>

<section class="slide col-r r1">
  <div class="photo" role="img" aria-label="Worker in orange high-visibility shirt and hard hat on site" style="right:0;top:0;width:230px;height:308px;background:linear-gradient(160deg,#d7dde2,#e07a2c 55%,#5b4b3d)"></div>
  <div class="brand" style="left:22px;top:20px"><i></i>velqor</div>
  <div class="h" style="left:22px;top:64px;font-size:26px">Personnel<br><b>Tracking<br>Solutions</b></div>
  <div class="txt" style="left:22px;top:160px;width:250px">Locate crews, equipment and vehicles in real time and keep every shift safe underground.</div>
  <div class="txt" style="left:22px;top:210px"><span class="lbl">+4.1K</span>Workers tracked</div>
  <div class="btn" style="left:170px;top:212px">learn more today</div>
</section>

<!-- Row 2 -->
<section class="slide col-l r2">
  <div class="band" style="left:0;top:0;width:548px;height:44px"></div>
  <div class="brand" style="left:22px;top:16px"><i></i>velqor</div>
  <svg style="position:absolute;left:34px;top:80px" width="190" height="190" viewBox="0 0 190 190">
    <circle cx="95" cy="95" r="62" fill="none" stroke="var(--mid)" stroke-width="1"/>
    <circle cx="95" cy="95" r="34" fill="var(--blue)"/>
    <circle cx="95" cy="33" r="10" fill="var(--ink)"/><circle cx="157" cy="95" r="10" fill="var(--blue)"/>
    <circle cx="95" cy="157" r="10" fill="var(--ink)"/><circle cx="33" cy="95" r="10" fill="var(--blue)"/>
  </svg>
  <div class="h" style="left:270px;top:66px;font-size:22px">About <b>Us</b></div>
  <div class="txt" style="left:270px;top:104px;width:250px"><span class="lbl">We are experts in IoT based site tracking</span>We design systems that identify, monitor and locate people and assets in demanding sites.</div>
  <div class="txt" style="left:270px;top:170px;width:250px"><span class="lbl">Improved Efficiency and more solutions</span>One platform brings safety, productivity and reporting together for mining and tunnelling teams.</div>
</section>

<section class="slide col-r r2">
  <div class="brand" style="right:22px;top:16px"><i></i>velqor</div>
  <div class="h" style="left:22px;top:56px;font-size:22px">how does it<br>work</div>
  <div class="txt" style="left:22px;top:120px;width:200px"><span class="lbl blue">01. Tracking Tag</span>Worn by each worker or fitted to assets.</div>
  <div class="txt" style="left:22px;top:165px;width:200px"><span class="lbl blue">02. Data Processing</span>Readers and gateways send positions.</div>
  <div class="txt" style="left:22px;top:210px;width:200px"><span class="lbl blue">03. Application</span>Live maps, alerts and reports.</div>
  <div class="photo" role="img" aria-label="Illustration of tags, gateways and dashboards on laptop, tablet and phone" style="left:250px;top:40px;width:280px;height:240px;background:radial-gradient(circle at 50% 50%,#dfeaf2,#f4f6f8 70%)"></div>
</section>

<!-- Row 3 -->
<section class="slide col-l r3" style="background:var(--grey)">
  <div class="brand" style="right:22px;top:16px"><i></i>velqor</div>
  <div class="h" style="left:22px;top:24px;font-size:20px;color:var(--blue)">SYSTEM<br>ARCHITECTURE:</div>
  <div class="txt" style="left:22px;top:90px;line-height:2.9">
    <div><span class="dot"></span>Workers</div><div><span class="dot"></span>Vehicles</div><div><span class="dot"></span>Readers</div><div><span class="dot"></span>Gateway</div><div><span class="dot"></span>Server</div>
  </div>
  <div class="photo" role="img" aria-label="Isometric illustration of a mine site with readers, vehicles and control room" style="left:180px;top:60px;width:350px;height:230px;background:linear-gradient(135deg,#f3e3c4,#d9b57c 50%,#9aa7b1)"></div>
</section>

<section class="slide col-r r3">
  <div class="band" style="left:0;top:0;width:220px;height:308px;background:var(--ink)"></div>
  <div class="h" style="left:22px;top:40px;font-size:20px;color:var(--white)">Features &amp;<br><b>Benefits</b></div>
  <div class="txt" style="left:22px;top:100px;width:170px;color:#c6ced4">Simple tags, complete coverage and clear insight.</div>
  <div class="photo" role="img" aria-label="Black oval tracking tag device" style="left:60px;top:170px;width:150px;height:80px;border-radius:40px;background:radial-gradient(circle at 40% 35%,#5a5f63,#111)"></div>
  <div class="txt" style="left:250px;top:28px;width:200px;line-height:1.4">
    <div style="margin-bottom:10px"><span class="lbl">Personnel tracking</span>Know who is where at all times.</div>
    <div style="margin-bottom:10px"><span class="lbl">Asset location</span>Find equipment fast.</div>
    <div style="margin-bottom:10px"><span class="lbl">Vehicle monitoring</span>Avoid collisions underground.</div>
    <div style="margin-bottom:10px"><span class="lbl">Emergency alerts</span>One press raises an alarm.</div>
    <div><span class="lbl">Reporting</span>Shift data in one place.</div>
  </div>
  <div class="photo" role="img" aria-label="Phone showing tracking app screens" style="left:470px;top:30px;width:60px;height:110px;border-radius:8px;background:linear-gradient(#1e9ad6,#dfeaf2)"></div>
</section>

<!-- Row 4 -->
<section class="slide col-l r4">
  <div class="band" style="left:0;top:0;width:220px;height:308px"></div>
  <div class="photo" role="img" aria-label="Black tracking tag device on grey" style="left:40px;top:60px;width:150px;height:90px;border-radius:44px;background:radial-gradient(circle at 40% 35%,#5a5f63,#111)"></div>
  <div class="band" style="left:20px;top:200px;width:180px;height:80px;background:var(--ink)"></div>
  <div class="txt" style="left:34px;top:218px;width:150px;color:var(--white)"><span class="lbl" style="color:var(--white)">Dual-band tag</span>Long battery, rugged shell</div>
  <div class="brand" style="right:22px;top:16px"><i></i>velqor</div>
  <div class="h" style="left:250px;top:70px;font-size:20px">software &amp;<br>hardware specs</div>
  <div class="txt" style="left:250px;top:130px;width:260px">IP67 rated housing, up to two years battery, BLE and UWB positioning, and a web platform with live maps, alerts and shift reports.</div>
</section>

<section class="slide col-r r4">
  <div class="brand" style="left:22px;top:16px"><i></i>velqor</div>
  <div class="h" style="left:22px;top:46px;font-size:20px">Single device,<br><b>Multiple<br>solutions</b></div>
  <div class="photo" role="img" aria-label="Miner working in a narrow tunnel" style="left:330px;top:0;width:218px;height:140px;background:linear-gradient(140deg,#2a3138,#7b6850)"></div>
  <div class="txt" style="left:22px;top:160px;width:300px;display:grid;grid-template-columns:1fr 1fr;gap:14px">
    <div><span class="lbl">Lamp tracking</span>Tag fits the cap lamp.</div>
    <div><span class="lbl">Vehicle alerts</span>Proximity warnings.</div>
    <div><span class="lbl">Mustering</span>Fast headcounts.</div>
    <div><span class="lbl">Access control</span>Zone entry logs.</div>
  </div>
  <div class="txt" style="left:350px;top:190px"><span class="lbl blue" style="font-size:14px">200m+</span>Reading range</div>
</section>

<!-- Row 5 -->
<section class="slide col-l r5">
  <div class="photo" role="img" aria-label="Portrait of a site worker in hard hat" style="left:0;top:0;width:150px;height:150px;background:linear-gradient(150deg,#e8d7c1,#e07a2c)"></div>
  <div class="photo" role="img" aria-label="Tunnel boring site" style="left:0;top:158px;width:150px;height:150px;background:linear-gradient(150deg,#3a4650,#9a8a6c)"></div>
  <div class="brand" style="right:22px;top:16px"><i></i>velqor</div>
  <div class="h" style="left:175px;top:40px;font-size:20px">Case <b>Studies</b></div>
  <div class="txt" style="left:175px;top:90px;width:350px;display:grid;grid-template-columns:1fr 1fr;gap:18px 20px">
    <div><span class="lbl blue">01. Introduction</span>Site needs and goals.</div>
    <div><span class="lbl blue">02. Client Background</span>Deep gold mine operator.</div>
    <div><span class="lbl blue">03. Problem Statement</span>No live crew visibility.</div>
    <div><span class="lbl blue">04. Detailed Solution</span>Tags, readers, dashboard.</div>
  </div>
</section>

<section class="slide col-r r5">
  <div class="brand" style="right:22px;top:16px"><i></i>velqor</div>
  <div class="h" style="left:22px;top:30px;font-size:20px">Testimonials</div>
  <div class="badge" style="left:22px;top:80px;width:90px;height:36px;background:#f2a63a"></div>
  <div class="badge" style="left:22px;top:126px;width:90px;height:36px;background:#d7292e"></div>
  <div class="photo" role="img" aria-label="Two engineers reviewing plans on site" style="left:150px;top:60px;width:200px;height:200px;background:linear-gradient(150deg,#c9b79b,#e07a2c 60%,#4c4137)"></div>
  <div class="txt" style="left:370px;top:70px;width:160px">
    <div style="margin-bottom:16px"><span class="lbl">Site Manager</span>"Headcounts now take seconds, not hours."</div>
    <div><span class="lbl">Safety Lead</span>"Our crews feel safer every shift."</div>
  </div>
</section>

<!-- Row 6 -->
<section class="slide col-l r6">
  <div class="photo" role="img" aria-label="Tunnel entrance at dusk" style="left:0;top:0;width:150px;height:308px;background:linear-gradient(180deg,#d6dde3,#3b4650)"></div>
  <div class="h" style="left:22px;top:60px;font-size:20px;color:var(--white)">Our<br><b>Pricing</b></div>
  <div class="price" style="left:180px"><h4>Basic</h4><p>Tags<br>Readers<br>Web app</p><span class="go">select</span></div>
  <div class="price pro" style="left:280px"><h4>Professional</h4><p>Tags<br>Readers<br>Alerts<br>Reports</p><span class="go">select</span></div>
  <div class="price" style="left:380px"><h4>Enterprise</h4><p>Full site<br>Support<br>Custom</p><span class="go">select</span></div>
  <div class="brand" style="right:22px;top:16px"><i></i>velqor</div>
</section>

<section class="slide col-r r6" style="background:var(--tunnel-a)">
  <div class="photo" role="img" aria-label="Lit tunnel interior with rail tracks" style="inset:0;background:radial-gradient(circle at 50% 45%,#f1c98a 0%,#8a6b49 22%,#2b2f33 60%,#12181d 100%)"></div>
  <div class="brand light" style="left:50%;transform:translateX(-50%);top:24px"><i></i>velqor</div>
  <div class="h" style="left:0;width:548px;text-align:center;top:112px;font-size:50px;color:var(--blue)">THANKS</div>
  <div class="contact" style="left:169px;top:240px">
    <div>E-mail<span>info@velqor</span></div><div class="on">Website<span>velqor.example</span></div><div>Phone<span>000 000 000</span></div>
  </div>
</section>

</body>
</html>
```